updating a virtual bank "pop-up" branch banner

we need to make this more modern looking. remove the woman please. make it look like 2022 and not 1980.

```html
<!DOCTYPE html>
<html lang="en">
<head>
<meta charset="utf-8">
<title>Smart POS – Pop-up Branch Banner</title>
<link href="https://fonts.googleapis.com/css2?family=Roboto+Condensed:wght@300;400;700&display=swap" rel="stylesheet">
<style>
  :root {
    --canvas: #ffffff;
    --navy: #0a1228;
    --navy-mid: #13254a;
    --wave: #2d5580;
    --wave-light: #4a7fb0;
    --accent: #1b96c0;
    --accent-soft: rgba(27, 150, 192, 0.16);
    --white: #ffffff;
    --muted: #9fb4cc;
    --machine-a: #c9cdd3;
    --machine-b: #3a3f4a;
  }
  * { margin: 0; padding: 0; box-sizing: border-box; }
  html, body {
    width: 1200px; height: 1200px; overflow: hidden;
    background: var(--canvas);
  }
  .banner {
    position: absolute;
    left: 278px; top: 86px;
    width: 644px; height: 1028px;
    overflow: hidden;
    border-radius: 20px;
    background: linear-gradient(160deg, var(--navy-mid) 0%, var(--navy) 55%);
    font-family: "Roboto Condensed", sans-serif;
  }
  .banner-shapes { position: absolute; inset: 0; }
  .brand {
    position: absolute; left: 40px; top: 42px;
    display: flex; align-items: center; gap: 12px;
    font-weight: 700; font-size: 36px; line-height: 1;
    color: var(--white); letter-spacing: 0.5px;
  }
  .brand-mark { width: 16px; height: 16px; border-radius: 50%; background: var(--accent); }
  .headline {
    position: absolute; left: 40px; top: 118px;
    color: var(--white); line-height: 0.92;
  }
  .headline-light { display: block; font-weight: 300; font-size: 76px; letter-spacing: -1px; }
  .headline-bold { display: block; font-weight: 700; font-size: 124px; letter-spacing: -2px; color: var(--white); }
  .headline-bold::after {
    content: ""; display: block; width: 64px; height: 6px; margin-top: 14px;
    border-radius: 3px; background: var(--accent);
  }
  .feature-list { position: absolute; left: 40px; top: 396px; list-style: none; }
  .feature-pill {
    width: 262px; height: 48px; margin-bottom: 14px;
    padding: 0 18px 0 10px;
    border-radius: 24px;
    background: var(--accent-soft);
    border: 1px solid rgba(27, 150, 192, 0.45);
    color: var(--white);
    font-size: 23px; font-weight: 400;
    display: flex; align-items: center; gap: 14px;
  }
  .feature-icon { width: 30px; height: 30px; flex: none; }
  .machine-photo { position: absolute; left: 346px; top: 300px; }
</style>
</head>
<body>
  <section class="banner">
    <svg class="banner-shapes" viewBox="0 0 644 1028" width="644" height="1028">
      <defs>
        <linearGradient id="waveTone" x1="0" y1="1" x2="1" y2="0">
          <stop offset="0" stop-color="var(--navy-mid)"/>
          <stop offset="1" stop-color="var(--wave)"/>
        </linearGradient>
      </defs>
      <circle cx="560" cy="120" r="230" fill="none" stroke="var(--wave-light)" stroke-width="1" opacity="0.35"/>
      <circle cx="560" cy="120" r="160" fill="var(--accent)" opacity="0.08"/>
      <path d="M0 1028 C170 960 400 880 644 850 L644 1028 Z" fill="url(#waveTone)" opacity="0.85"/>
      <path d="M0 1028 C220 980 440 950 644 948 L644 1028 Z" fill="var(--navy)"/>
      <path d="M0 1010 C200 930 430 870 644 840" fill="none" stroke="var(--wave-light)" stroke-width="2" opacity="0.7"/>
    </svg>

    <div class="brand"><span class="brand-mark"></span>vittaro</div>

    <h1 class="headline">
      <span class="headline-light">Smart</span>
      <span class="headline-bold">POS</span>
    </h1>

    <ul class="feature-list">
      <li class="feature-pill"><svg class="feature-icon" viewBox="0 0 30 30"><circle cx="15" cy="15" r="15" fill="var(--accent)"/><path d="M9 15.5l4 4 8-9" fill="none" stroke="var(--white)" stroke-width="2.6" stroke-linecap="round" stroke-linejoin="round"/></svg>Feature 1</li>
      <li class="feature-pill"><svg class="feature-icon" viewBox="0 0 30 30"><circle cx="15" cy="15" r="15" fill="var(--accent)"/><path d="M9 15.5l4 4 8-9" fill="none" stroke="var(--white)" stroke-width="2.6" stroke-linecap="round" stroke-linejoin="round"/></svg>Feature 2</li>
      <li class="feature-pill"><svg class="feature-icon" viewBox="0 0 30 30"><circle cx="15" cy="15" r="15" fill="var(--accent)"/><path d="M9 15.5l4 4 8-9" fill="none" stroke="var(--white)" stroke-width="2.6" stroke-linecap="round" stroke-linejoin="round"/></svg>Feature 3</li>
      <li class="feature-pill"><svg class="feature-icon" viewBox="0 0 30 30"><circle cx="15" cy="15" r="15" fill="var(--accent)"/><path d="M9 15.5l4 4 8-9" fill="none" stroke="var(--white)" stroke-width="2.6" stroke-linecap="round" stroke-linejoin="round"/></svg>Feature 4</li>
      <li class="feature-pill"><svg class="feature-icon" viewBox="0 0 30 30"><circle cx="15" cy="15" r="15" fill="var(--accent)"/><path d="M9 15.5l4 4 8-9" fill="none" stroke="var(--white)" stroke-width="2.6" stroke-linecap="round" stroke-linejoin="round"/></svg>Feature 5</li>
      <li class="feature-pill"><svg class="feature-icon" viewBox="0 0 30 30"><circle cx="15" cy="15" r="15" fill="var(--accent)"/><path d="M9 15.5l4 4 8-9" fill="none" stroke="var(--white)" stroke-width="2.6" stroke-linecap="round" stroke-linejoin="round"/></svg>Feature 6</li>
      <li class="feature-pill"><svg class="feature-icon" viewBox="0 0 30 30"><circle cx="15" cy="15" r="15" fill="var(--accent)"/><path d="M9 15.5l4 4 8-9" fill="none" stroke="var(--white)" stroke-width="2.6" stroke-linecap="round" stroke-linejoin="round"/></svg>Feature 7</li>
      <li class="feature-pill"><svg class="feature-icon" viewBox="0 0 30 30"><circle cx="15" cy="15" r="15" fill="var(--accent)"/><path d="M9 15.5l4 4 8-9" fill="none" stroke="var(--white)" stroke-width="2.6" stroke-linecap="round" stroke-linejoin="round"/></svg>Feature 8</li>
    </ul>

    <svg class="machine-photo" width="262" height="560" viewBox="0 0 262 560" role="img" aria-label="Photo of a cash machine kiosk">
      <defs>
        <linearGradient id="machineTone" x1="0" y1="0" x2="1" y2="0">
          <stop offset="0" stop-color="var(--machine-a)"/>
          <stop offset="0.55" stop-color="#6b717c"/>
          <stop offset="1" stop-color="var(--machine-b)"/>
        </linearGradient>
      </defs>
      <rect x="0" y="0" width="262" height="560" rx="26" fill="url(#machineTone)"/>
    </svg>
  </section>
</body>
</html>
```